Quiet Meadow Counseling business cards

Dana Korvath, LCPC, NCC
(555)347-0618
www.quietmeadowcounseling.example
dana@quietmeadowcounseling.example

Business cards. I would like it on the same background as pictured. Not on a white business card. I have attached the logo that was done by another designer with artbazaar. I am open to looking at single-sided and double-sided designs.

Target Market(s)

teenagers and adults

Industry/Entity Type

mental health

Contact Information for Business Card

Dana Korvath, LCPC, NCC (555)347-0618 dana@quietmeadowcounseling.example

Font styles to use
Other font styles liked:
• Cinzel

Colors

Designer to choose colors to be used in the design.

Requirements
Must have
• logo that is attached

```html
<!DOCTYPE html>
<html lang="en">
<head>
<meta charset="UTF-8">
<title>Quiet Meadow Counseling — Business Card</title>
<link rel="stylesheet" href="https://fonts.googleapis.com/css2?family=Montserrat:wght@400;500;600;700&display=swap">
<style>
  :root {
    --backdrop: #6a7b7d;
    --card-deep: #0f1c26;
    --card-mid: #1a2d3a;
    --brand-blue: #1d4f9e;
    --silver: #c4cfd0;
    --soft-white: #e3e9ea;
    --mint: #4fd49a;
    --teal: #3f8ea3;
    --band: #1f3a4b;
  }
  * { margin: 0; padding: 0; box-sizing: border-box; }
  html, body {
    width: 1200px; height: 1200px; overflow: hidden;
    background: var(--backdrop);
    font-family: "Montserrat", sans-serif;
  }
  .card {
    position: absolute; left: 155px; top: 345px;
    width: 890px; height: 509px; overflow: hidden;
    background:
      radial-gradient(ellipse 60% 70% at 72% 20%, rgba(40,64,80,0.55), transparent 70%),
      linear-gradient(100deg, var(--card-deep) 0%, #132330 45%, var(--card-mid) 75%, #142430 100%);
  }
  .brand-mark {
    position: absolute; left: 178px; top: 66px;
    width: 134px; height: 134px; border-radius: 50%;
    background: var(--teal);
  }
  .brand-name {
    position: absolute; left: 64px; top: 222px; width: 366px;
    text-align: center; color: var(--brand-blue);
    font-weight: 700; font-size: 27px; line-height: 34px;
    letter-spacing: -0.5px; text-transform: uppercase;
  }
  .divider {
    position: absolute; left: 488px; top: 219px; height: 66px;
    border-left: 1px dotted rgba(196,207,208,0.5);
  }
  .person { position: absolute; left: 547px; top: 220px; }
  .person-name {
    color: var(--silver); font-weight: 600; font-size: 38px;
    letter-spacing: 2px; line-height: 44px;
  }
  .person-creds {
    color: var(--silver); font-weight: 400; font-size: 22px;
    letter-spacing: 1px; margin-top: 2px;
  }
  .leaf-band {
    position: absolute; left: 0; top: 335px; width: 890px; height: 34px;
    background: linear-gradient(90deg, #223442, #1e3a3e, #2a3446, #1d3a44, #223442);
    opacity: 0.85;
  }
  .stripe {
    position: absolute; left: 0; top: 369px; width: 890px; height: 16px;
    background: var(--band);
  }
  .contact {
    position: absolute; top: 434px; display: flex; align-items: center;
    color: var(--soft-white); font-size: 21px; font-weight: 400; letter-spacing: 0.6px;
  }
  .contact svg { margin-right: 20px; flex: none; }
  .contact-phone { left: 62px; }
  .contact-email { left: 344px; }
</style>
</head>
<body>
  <div class="card">
    <div class="brand-mark"></div>
    <div class="brand-name">Quiet Meadow Counseling</div>

    <div class="divider"></div>

    <div class="person">
      <div class="person-name">DANA KORVATH</div>
      <div class="person-creds">LCPC, NCC</div>
    </div>

    <div class="leaf-band" role="img" aria-label="Row of small multicoloured leaf shapes"></div>
    <div class="stripe"></div>

    <div class="contact contact-phone">
      <svg width="20" height="20" viewBox="0 0 24 24" aria-hidden="true">
        <path fill="var(--mint)" d="M6.6 2.5c.6-.4 1.4-.2 1.8.4l2 3.2c.4.6.2 1.4-.3 1.8L8.6 9c.9 2.6 3.6 5.5 6.4 6.5l1.3-1.5c.5-.5 1.3-.6 1.8-.2l3.1 2.2c.6.4.8 1.2.4 1.8l-1.3 2.1c-.7 1.1-2 1.6-3.3 1.3C9.9 19.6 4.3 14 2.7 7.1c-.3-1.3.2-2.6 1.3-3.3z"/>
      </svg>
      <span>(555) 347-0618</span>
    </div>

    <div class="contact contact-email">
      <svg width="22" height="16" viewBox="0 0 22 16" aria-hidden="true">
        <rect x="0" y="0" width="22" height="16" fill="var(--mint)"/>
        <path d="M1 1 L11 9 L21 1" fill="none" stroke="var(--card-deep)" stroke-width="2"/>
      </svg>
      <span>dana@quietmeadowcounseling.example</span>
    </div>
  </div>
</body>
</html>
```